Quillory Nest Business Card

I need a business card design. We are a collaborate online training company. Our colors are gray and green. Our website is QuilloryNest.com

I would like an area for a profile picture within the card

```html
<!DOCTYPE html>
<html lang="en">
<head>
<meta charset="utf-8">
<title>Quillory Nest Business Card</title>
<link href="https://fonts.googleapis.com/css2?family=Arimo:ital,wght@0,400;0,700;1,400&family=Roboto+Condensed:wght@700&display=swap" rel="stylesheet">
<style>
  :root {
    --canvas: #e9ebec;
    --card-dark: #2b2d2e;
    --card-light: #ffffff;
    --brand-green: #86f22a;
    --ink: #111111;
    --text-light: #ffffff;
    --photo-top: #4a4b4c;
    --photo-bottom: #b9a892;
  }
  * { margin: 0; padding: 0; box-sizing: border-box; }
  html, body {
    width: 1200px;
    height: 1200px;
    overflow: hidden;
    background: var(--canvas);
  }
  .sheet {
    position: relative;
    width: 1200px;
    height: 1200px;
  }
  .card {
    position: absolute;
    left: 150px;
    width: 900px;
    height: 515px;
    display: block;
    box-shadow: 0 6px 18px rgba(0,0,0,0.12);
  }
  .card--front { top: 50px; }
  .card--back { top: 630px; }
  .brand-name {
    font-family: "Roboto Condensed", "Arial Narrow", sans-serif;
    font-weight: 700;
    fill: var(--ink);
  }
  .holder-name {
    font-family: "Arimo", Arial, sans-serif;
    font-weight: 700;
    fill: var(--text-light);
  }
  .holder-role {
    font-family: "Arimo", Arial, sans-serif;
    font-style: italic;
    fill: var(--text-light);
  }
  .contact-text {
    font-family: "Arimo", Arial, sans-serif;
    fill: var(--text-light);
  }
  .fill-dark { fill: var(--card-dark); }
  .fill-light { fill: var(--card-light); }
  .fill-green { fill: var(--brand-green); }
  .icon-mark { fill: var(--text-light); }
  .icon-line { fill: none; stroke: var(--text-light); stroke-width: 1.4; }
  .photo-frame { fill: none; stroke: var(--text-light); stroke-width: 3; }
</style>
</head>
<body>
<main class="sheet">

  <!-- Front side -->
  <svg class="card card--front" viewBox="0 0 598 342" aria-label="Business card front">
    <defs>
      <linearGradient id="photoTone" x1="0" y1="0" x2="0" y2="1">
        <stop offset="0" stop-color="var(--photo-top)"/>
        <stop offset="1" stop-color="var(--photo-bottom)"/>
      </linearGradient>
    </defs>
    <rect class="fill-light" width="598" height="342"/>
    <g class="edge-stripes">
      <rect class="fill-dark" x="540" y="0" width="12" height="342"/>
      <rect class="fill-green" x="554" y="0" width="6" height="342"/>
      <rect class="fill-dark" x="562" y="0" width="12" height="342"/>
    </g>
    <g class="brand-lockup">
      <circle class="fill-green" cx="88" cy="171" r="30"/>
      <text class="brand-name" x="132" y="190" font-size="54">Quillory Nest</text>
    </g>
  </svg>

  <!-- Back side -->
  <svg class="card card--back" viewBox="0 0 598 342" aria-label="Business card back">
    <defs>
      <linearGradient id="photoToneBack" x1="0" y1="0" x2="0" y2="1">
        <stop offset="0" stop-color="#4a4b4c"/>
        <stop offset="1" stop-color="#b9a892"/>
      </linearGradient>
    </defs>
    <rect class="fill-dark" width="598" height="342"/>

    <g class="accent-lines">
      <rect class="fill-green" x="33" y="0" width="8" height="180"/>
      <rect class="fill-green" x="48" y="0" width="8" height="180"/>
    </g>

    <text class="holder-name" x="81" y="49" font-size="23">YOUR NAME</text>
    <text class="holder-role" x="81" y="69" font-size="16">Position</text>

    <rect role="img" aria-label="Profile photo of the card holder" x="358" y="28" width="193" height="166" fill="url(#photoToneBack)"/>
    <rect class="photo-frame" x="358" y="28" width="193" height="166"/>

    <g class="contact-address">
      <circle class="fill-green" cx="46" cy="207" r="17"/>
      <path class="icon-mark" d="M46 197a6 6 0 0 0-6 6c0 5 6 12 6 12s6-7 6-12a6 6 0 0 0-6-6zm0 8.3a2.3 2.3 0 1 1 0-4.6 2.3 2.3 0 0 1 0 4.6z"/>
      <text class="contact-text" x="82" y="205" font-size="14">Street Name, Number,</text>
      <text class="contact-text" x="82" y="222" font-size="14">City, Zip Code</text>
    </g>

    <g class="contact-phone">
      <circle class="fill-green" cx="46" cy="259" r="17"/>
      <path class="icon-mark" d="M40.5 250.5l3.2-0.8 2 4.6-2.2 1.6c1 2.3 2.8 4.2 5.2 5.3l1.6-2.2 4.6 2-0.8 3.2c-0.3 1-1.3 1.6-2.3 1.4-6.2-1.2-11.2-6-12.4-12.3-0.2-1 0.3-2.5 1.1-2.8z"/>
      <text class="contact-text" x="82" y="264" font-size="14">555 555 555</text>
    </g>

    <g class="contact-email">
      <circle class="fill-green" cx="46" cy="312" r="17"/>
      <rect class="icon-mark" x="36" y="305" width="20" height="14" rx="1"/>
      <path d="M36.5 305.5l9.5 7.5 9.5-7.5M36.5 318.5l7-6M55.5 318.5l-7-6" fill="none" stroke="var(--brand-green)" stroke-width="1.4"/>
      <text class="contact-text" x="82" y="317" font-size="14">yourname@email.com</text>
    </g>

    <g class="contact-web">
      <text class="contact-text" x="481" y="299" font-size="14" text-anchor="end">www.quillorynest.com</text>
      <circle class="fill-green" cx="506" cy="294" r="16"/>
      <circle class="icon-line" cx="506" cy="294" r="9"/>
      <ellipse class="icon-line" cx="506" cy="294" rx="4" ry="9"/>
      <path class="icon-line" d="M497 294h18M498.5 289.5h15M498.5 298.5h15M506 285v18"/>
      <rect class="fill-green" x="532" y="285" width="66" height="6"/>
      <rect class="fill-green" x="532" y="299" width="66" height="7"/>
    </g>
  </svg>

</main>
</body>
</html>
```